I need a design for Corvane Homes which is a custom home builder. The name on it will be Dan Hartley, and I will give the phone number to the winning design. No address or website needed.

```html
<!DOCTYPE html>
<html lang="en">
<head>
<meta charset="UTF-8">
<title>Corvane Homes – Business Card</title>
<link rel="stylesheet" href="https://fonts.googleapis.com/css2?family=Poiret+One&display=swap">
<style>
  :root {
    --page-bg: #ffffff;
    --navy-deep: #252c60;
    --navy-mid: #4f5a98;
    --periwinkle: #8c9ee0;
    --periwinkle-glow: #a8b8f6;
    --card-white: #ffffff;
    --ink: #4b5083;
    --house-light: #eef0f4;
    --house-mid: #d3d6de;
    --house-dark: #bfc3cd;
    --card-edge: rgba(0, 0, 0, 0.35);
  }
  * { box-sizing: border-box; margin: 0; padding: 0; }
  html, body {
    width: 910px;
    height: 1200px;
    overflow: hidden;
    background: var(--page-bg);
  }
  .sheet {
    position: relative;
    width: 910px;
    height: 1200px;
  }
  .card {
    position: absolute;
    left: 78px;
    width: 759px;
    height: 445px;
    overflow: hidden;
    box-shadow: 2px 3px 4px var(--card-edge);
  }
  .card--front {
    top: 81px;
    background:
      radial-gradient(ellipse 60% 55% at 50% 88%, var(--periwinkle-glow) 0%, rgba(168,184,246,0) 100%),
      linear-gradient(180deg, var(--navy-deep) 0%, var(--navy-mid) 45%, var(--periwinkle) 100%);
    display: flex;
    align-items: center;
    justify-content: center;
  }
  .brand-name {
    font-family: "Poiret One", sans-serif;
    font-size: 60px;
    letter-spacing: 2px;
    color: var(--card-white);
    text-transform: uppercase;
    margin-top: 40px;
  }
  .card--back {
    top: 685px;
    background: var(--card-white);
    border: 1px solid #e6e6ea;
  }
  .house-art {
    position: absolute;
    inset: 0;
    background: linear-gradient(160deg, var(--house-light) 0%, var(--house-mid) 55%, var(--house-dark) 100%);
    clip-path: polygon(0% 100%, 0% 60%, 34% 8%, 44% 24%, 96% 100%);
  }
  .contact {
    position: absolute;
    right: 38px;
    top: 84px;
    text-align: right;
    font-family: "Poiret One", sans-serif;
    color: var(--ink);
    text-transform: uppercase;
  }
  .contact__name {
    font-size: 31px;
    letter-spacing: 2px;
    line-height: 1;
  }
  .contact__phone {
    font-size: 31px;
    letter-spacing: 3px;
    line-height: 1;
    margin-top: 24px;
  }
</style>
</head>
<body>
  <main class="sheet">
    <section class="card card--front">
      <h1 class="brand-name">Corvane Homes</h1>
    </section>
    <section class="card card--back">
      <div class="house-art" role="img" aria-label="Soft grey silhouettes of overlapping house roofs"></div>
      <div class="contact">
        <p class="contact__name">Dan Hartley</p>
        <p class="contact__phone">066 - 555201734</p>
      </div>
    </section>
  </main>
</body>
</html>
```